Desing for real estate offers- Package system

The word should be graphically clear and understandable. There are 3 packages that the customer can buy: the basic package is red, the medicinal package is green and the carefree package is blue. See the Word document in the appendix. End file should be a Word, as we need to chance the text. It should also match the website as well as the business card.
https://brelvona.domistra.ch/
Colors:
Green 1: R: 187, G: 214, B: 49
Green 2: R: 119, G: 187, W: 66

Target Market(s)

Real estate company

Font styles to use
Serif
Sans Serif

```html
<!DOCTYPE html>
<html lang="de">
<head>
<meta charset="utf-8">
<title>Vermarktungspakete – Brelvona</title>
<link rel="stylesheet" href="https://fonts.googleapis.com/css2?family=Outfit:wght@400;500&family=Saira+Condensed:wght@400;500;600&display=swap">
<style>
:root{
  --green-1:#bbd631;
  --green-2:#77bb42;
  --green-text:#9bb824;
  --green-dark:#6e8c14;
  --orange-box:#f4a27c;
  --orange-text:#ee7446;
  --orange-dark:#c9532a;
  --blue-box:#a7d8f4;
  --blue-text:#0f86c8;
  --ink:#2b2b2b;
  --paper:#ffffff;
  --stage:#ffffff;
}
*{margin:0;padding:0;box-sizing:border-box}
html,body{width:1200px;height:720px;overflow:hidden;background:var(--stage)}
body{position:relative;font-family:"Saira Condensed",sans-serif;color:var(--ink)}

.sheet{position:absolute;background:var(--paper);overflow:hidden;box-shadow:0 0 0 1px #f0f0f0}
.sheet--sorglos{left:82px;top:64px;width:414px;height:583px;--c-box:var(--green-1);--c-text:var(--green-text);--c-logo:var(--green-dark)}
.sheet--medium{left:809px;top:202px;width:317px;height:447px;--c-box:var(--blue-box);--c-text:var(--blue-text);--c-logo:#ffffff}
.sheet--basis{left:526px;top:64px;width:313px;height:443px;--c-box:var(--orange-box);--c-text:var(--orange-text);--c-logo:var(--orange-dark)}

.sheet > *{position:absolute}
.title{font-family:"Outfit",sans-serif;font-weight:500;color:var(--c-text);line-height:1;text-align:right;white-space:nowrap}
.subtitle{font-weight:400;letter-spacing:.4px;color:var(--ink);line-height:1;white-space:nowrap}
.accent-bar{background:var(--c-box)}
.photo{background:linear-gradient(100deg,#e9e6df 0%,#f4f2ed 35%,#d8d2c7 60%,#8c7d6d 78%,#e7e2da 100%)}
.brand-box{background:var(--c-box);text-align:center;color:#fff}
.brand-name{font-family:"Outfit",sans-serif;font-weight:500;color:var(--c-logo);line-height:1;display:block}
.brand-tagline{display:block;line-height:1.1}
.brand-contact{display:block;line-height:1.35}
.price{color:var(--c-text);line-height:1;white-space:nowrap}
.price-main{font-family:"Outfit",sans-serif;font-weight:400}
.price-note{display:inline-block;vertical-align:top;line-height:1.05}
.terms{line-height:1.35}
.services{list-style:none}
.services li{position:relative}
.services li::before{content:"";position:absolute;background:var(--c-text);border-radius:50%}
.office{font-style:normal;border-left:1px solid var(--c-text);color:var(--c-text);font-weight:600;line-height:1.5;white-space:nowrap}

/* SORGLOS */
.sheet--sorglos .title{right:196px;top:56px;font-size:34px}
.sheet--sorglos .subtitle{left:237px;top:74px;font-size:10px}
.sheet--sorglos .accent-bar{left:0;top:103px;width:217px;height:15px}
.sheet--sorglos .photo{left:0;top:120px;width:414px;height:160px}
.sheet--sorglos .brand-box{left:0;top:241px;width:215px;height:127px;padding-top:36px}
.sheet--sorglos .brand-name{font-size:27px}
.sheet--sorglos .brand-tagline{font-size:11px;margin-top:6px}
.sheet--sorglos .brand-contact{font-size:7.4px;margin-top:10px}
.sheet--sorglos .price{left:106px;top:380px;width:200px}
.sheet--sorglos .price-main{font-size:32px}
.sheet--sorglos .price-main sup{font-size:15px;vertical-align:14px}
.sheet--sorglos .price-note{font-size:10.5px;margin:6px 0 0 4px}
.sheet--sorglos .price-footnote{left:106px;top:416px;font-size:6.4px;letter-spacing:.3px}
.sheet--sorglos .terms{left:59px;top:434px;width:160px;font-size:6.8px}
.sheet--sorglos .services{left:238px;top:298px;width:170px;font-size:6.8px;line-height:9.7px}
.sheet--sorglos .services li{padding-left:6px}
.sheet--sorglos .services li::before{left:0;top:4px;width:2.4px;height:2.4px}
.sheet--sorglos .office{top:493px;font-size:6.6px;padding-left:3px;height:45px;padding-top:5px}
.sheet--sorglos .office--a{left:59px}
.sheet--sorglos .office--b{left:137px}

/* BASIS + MEDIUM shared compact scale */
.sheet--basis .title,.sheet--medium .title{font-size:25px}
.sheet--basis .subtitle,.sheet--medium .subtitle{font-size:6.6px}
.sheet--basis .brand-name,.sheet--medium .brand-name{font-size:20px}
.sheet--basis .brand-tagline,.sheet--medium .brand-tagline{font-size:8.3px;margin-top:4px}
.sheet--basis .brand-contact,.sheet--medium .brand-contact{font-size:5.4px;margin-top:8px}
.sheet--basis .price-main,.sheet--medium .price-main{font-size:24px}
.sheet--basis .price-main sup,.sheet--medium .price-main sup{font-size:13px;vertical-align:10px}
.sheet--basis .price-note,.sheet--medium .price-note{position:absolute;top:15px;font-size:7.4px}
.sheet--basis .price-note{left:28px}
.sheet--medium .price-note{left:40px}
.sheet--basis .terms,.sheet--medium .terms{width:100px;font-size:4.9px;line-height:1.5}
.sheet--basis .services,.sheet--medium .services{width:110px;font-size:4.9px;line-height:7.4px}
.sheet--basis .services li,.sheet--medium .services li{padding-left:4px}
.sheet--basis .services li::before,.sheet--medium .services li::before{left:0;top:3px;width:1.8px;height:1.8px}
.sheet--basis .office,.sheet--medium .office{font-size:5px;padding-left:2px;height:27px;padding-top:2px}

/* BASIS */
.sheet--basis .title{right:149px;top:42px}
.sheet--basis .subtitle{left:179px;top:57px}
.sheet--basis .accent-bar{left:0;top:79px;width:164px;height:10px}
.sheet--basis .photo{left:0;top:91px;width:313px;height:123px}
.sheet--basis .brand-box{left:0;top:184px;width:163px;height:96px;padding-top:28px}
.sheet--basis .terms{left:181px;top:253px}
.sheet--basis .price{left:86px;top:294px}
.sheet--basis .services{left:181px;top:300px}
.sheet--basis .office{top:383px}
.sheet--basis .office--a{left:44px}
.sheet--basis .office--b{left:104px}

/* MEDIUM */
.sheet--medium .title{right:151px;top:44px}
.sheet--medium .subtitle{left:182px;top:58px}
.sheet--medium .accent-bar{left:0;top:78px;width:166px;height:13px}
.sheet--medium .photo{left:0;top:92px;width:317px;height:123px}
.sheet--medium .brand-box{left:0;top:185px;width:165px;height:98px;padding-top:28px}
.sheet--medium .terms{left:182px;top:256px}
.sheet--medium .price{left:77px;top:297px}
.sheet--medium .services{left:182px;top:303px}
.sheet--medium .office{top:385px}
.sheet--medium .office--a{left:47px}
.sheet--medium .office--b{left:107px}
</style>
</head>
<body>

<article class="sheet sheet--sorglos">
  <h1 class="title">SORGLOS</h1>
  <p class="subtitle">INDIVIDUELLE VERMARKTUNGSPAKET</p>
  <div class="accent-bar"></div>
  <div class="photo" role="img" aria-label="Foto: Familie betritt ein helles Wohnzimmer mit weissem Sofa"></div>
  <div class="brand-box">
    <span class="brand-name">Brelvona</span>
    <span class="brand-tagline">innovativ und individuell</span>
    <span class="brand-contact">tel +41 44 600 12 34<br>info@brelvona.ch &nbsp;&nbsp;&nbsp; www.brelvona.ch</span>
  </div>
  <p class="price"><span class="price-main">2<sup>%</sup></span><span class="price-note">vom Verkaufspreis<br>inkl. MWST</span></p>
  <p class="price-footnote">(von Grundstückgewinnsteuer abziehbar)</p>
  <p class="terms">Unterlagen müssen gestellt werden, ansonsten werden Sie 1:1 verrechnet: GB-Auszug,GVZ, Nebenkostenabrechnung, STWEG-Protokolle der letzten 3 Jahren, …</p>
  <ul class="services">
    <li>Begehung Verkaufsobjekt</li>
    <li>Hedonische Schätzung intern &amp; Bank</li>
    <li>Marketing &amp; Vertriebskonzept</li>
    <li>Unterlagen einfordern- STWEG Protokolle, GB Auszug u.s.w wenn nötig</li>
    <li>Fotografieren &amp; Ausmessen der Immobilie</li>
    <li>Grundriss zeichnen</li>
    <li>Dokumentation erstellen</li>
    <li>Unsere Interessenten anschreiben</li>
    <li>Immobilie Online aufbereiten &amp; Aufschalten</li>
    <li>Anfragen beantworten- telefonisch &amp; elektronisch</li>
    <li>Besichtigungen koordinieren</li>
    <li>Besichtigungen Durchführen</li>
    <li>Interessenten &amp; Kaufangebote prüfen</li>
    <li>Evt. Bieterverfahren modern oder altmodisch</li>
    <li>Käufer zusage- andere noch vertrösten</li>
    <li>Sicherheitsnachweis (SINA)- organisieren</li>
    <li>Erstellung erster Kaufvertragsentwurf</li>
    <li>Berechnung provisorische Grundstückgewinn-steuer-Steueramt</li>
    <li>Beurkundungstermin vereinbaren</li>
    <li>Begleitung aufs Notariat</li>
    <li>Eigentumsübertragung vereinbaren</li>
    <li>Helfen bei der Steuererklärung für die definitive Grundstückgewinnsteuer</li>
  </ul>
  <address class="office office--a">Externes Büro<br>Kantara Finanz GmbH<br>Lindenweg<br>8712 Seefeld</address>
  <address class="office office--b">Externes Sitzungszimmer<br>KRM<br>Mattenstrasse<br>8704 Talheim</address>
</article>

<article class="sheet sheet--medium">
  <h1 class="title">MEDIUM</h1>
  <p class="subtitle">INDIVIDUELLE VERMARKTUNGSPAKET</p>
  <div class="accent-bar"></div>
  <div class="photo" role="img" aria-label="Foto: Familie betritt ein helles Wohnzimmer mit weissem Sofa"></div>
  <div class="brand-box">
    <span class="brand-name">Brelvona</span>
    <span class="brand-tagline">innovativ und individuell</span>
    <span class="brand-contact">tel +41 44 600 12 34<br>info@brelvona.ch &nbsp;&nbsp; www.brelvona.ch</span>
  </div>
  <p class="terms">Unterlagen müssen gestellt werden, ansonsten werden Sie 1:1 verrechnet: GB-Auszug,GVZ, Nebenkostenabrechnung, STWEG-Protokolle der letzten 3 Jahren, …</p>
  <p class="price"><span class="price-main">10<sup>900</sup></span><span class="price-note">CHF exkl. MWST</span></p>
  <ul class="services">
    <li>Begehung Verkaufsobjekt</li>
    <li>Hedonische Schätzung intern &amp; Bank</li>
    <li>Marketing &amp; Vertriebskonzept</li>
    <li>Unterlagen einfordern- STWEG Protokolle, GB Auszug u.s.w wenn nötig</li>
    <li>Fotografieren &amp; Ausmessen der Immobilie</li>
    <li>Grundriss zeichnen</li>
    <li>Dokumentation erstellen</li>
    <li>Unsere Interessenten anschreiben</li>
    <li>Immobilie Online aufbereiten &amp; Aufschalten</li>
    <li>Interessenten &amp; Kaufangebote prüfen</li>
    <li>Evt. Bieterverfahren modern oder altmodisch</li>
    <li>Käufer zusage- andere noch vertrösten</li>
    <li>Erstellung erster Kaufvertragsentwurf</li>
    <li>Begleitung aufs Notariat</li>
  </ul>
  <address class="office office--a">Externes Büro<br>Kantara Finanz GmbH<br>Lindenweg<br>8712 Seefeld</address>
  <address class="office office--b">Externes Sitzungszimmer<br>KRM<br>Mattenstrasse<br>8704 Talheim</address>
</article>

<article class="sheet sheet--basis">
  <h1 class="title">BASIS</h1>
  <p class="subtitle">INDIVIDUELLE VERMARKTUNGSPAKET</p>
  <div class="accent-bar"></div>
  <div class="photo" role="img" aria-label="Foto: Kinder laufen durch einen hellen Wohnraum, Eltern im Hintergrund"></div>
  <div class="brand-box">
    <span class="brand-name">Brelvona</span>
    <span class="brand-tagline">innovativ und individuell</span>
    <span class="brand-contact">tel +41 44 600 12 34<br>info@brelvona.ch &nbsp;&nbsp; www.brelvona.ch</span>
  </div>
  <p class="terms">Unterlagen müssen gestellt werden, ansonsten werden Sie 1:1 verrechnet: GB-Auszug,GVZ, Nebenkostenabrechnung, STWEG-Protokolle der letzten 3 Jahren, …</p>
  <p class="price"><span class="price-main">8<sup>500</sup></span><span class="price-note">CHF exkl. MWST</span></p>
  <ul class="services">
    <li>Begehung Verkaufsobjekt</li>
    <li>Hedonische Schätzung intern &amp; Bank</li>
    <li>Marketing &amp; Vertriebskonzept</li>
    <li>Unterlagen einfordern- STWEG Protokolle, GB Auszug u.s.w wenn nötig</li>
    <li>Fotografieren &amp; Ausmessen der Immobilie</li>
    <li>Grundriss zeichnen</li>
    <li>Interessenten &amp; Kaufangebote prüfen</li>
    <li>Käufer zusage- andere noch vertrösten</li>
    <li>Erstellung erster Kaufvertragsentwurf</li>
  </ul>
  <address class="office office--a">Externes Büro<br>Kantara Finanz GmbH<br>Lindenweg<br>8712 Seefeld</address>
  <address class="office office--b">Externes Sitzungszimmer<br>KRM<br>Mattenstrasse<br>8704 Talheim</address>
</article>

</body>
</html>
```